Modern Yoga Studio Timetable and Flyer Design

We have a comprehensive class timetable and we are wanting to a clean modern look for our Spring timetable.

We require a double sided flyer with our class timetable included.
We would prefer an A5 size (postcard) or DL (1/3 A4).

We would like the final flyer to have.
Side A : Yoga image, logo

Fennel Stretch Hall
address: 4/71 Wexcombe Lane, Pelharton
website: fennelstretch.com.au
mobile: 0471 296 814

Side B: Clear easy to read timetable with a break down of class types and website.

We would also like to have a copy of the timetable itself as a separate jpg or pdf for use on our website to download.

Thank you.
Yours kindly,
Nell

I have attached a sample of another timetable of which I like the look and feel of, however this is just a guide. I've also attached our 'new' schedule in WORD plus uploaded our last design of the front.
Updates

Target Market(s)

Women aged 30-45

Industry/Entity Type

Health And Wellness

Font styles to use
Other font styles liked:
• Brandon Grotesque, Jenna Sue

Colors
6c459b
33a6d7
ffffff

Requirements
Must have
• A definitive colour to decipher between different class types on our timetable. Where each colour represents a different class type. Colours and layouts similar to our website design, see www.fennelstretch.com.au
Nice to have
• I've included a design of another studio whose timetable design I like. One of our own yoga images instead of a stock image.
Should not have
• No dark gridlines between the cells/boxes in the timetables. Please don't use stock yoga images.

```html
<!DOCTYPE html>
<html lang="en">
<head>
<meta charset="utf-8">
<title>Fennel Stretch Hall – Spring Timetable Flyer</title>
<link rel="stylesheet" href="https://fonts.googleapis.com/css2?family=Nunito+Sans:wght@400;600;700&family=Caveat:wght@400&family=Arimo:wght@400;700&display=swap">
<style>
:root{
  --stage:#fcd883;
  --purple:#6c459b;
  --purple-deep:#4b2d73;
  --blue:#33a6d7;
  --white:#ffffff;
  --ink:#2a2a2a;
  --rule:#3a3a3a;
  --star:#d6336c;
  --c-rise:#cde6a8;
  --c-vinyasa:#c4d8ef;
  --c-yin:#fbf0dc;
  --c-slow:#f8f0b0;
  --c-preg:#f7c48f;
  --c-mum:#d5c3e6;
  --c-kids-older:#f2a5aa;
  --c-kids-young:#bcb9dd;
  --c-teens:#cdb6df;
  --c-restore:#d3d3d3;
  --c-women:#ece8ef;
}
*{margin:0;padding:0;box-sizing:border-box}
html,body{width:900px;height:1200px;overflow:hidden}
body{background:var(--stage);position:relative;font-family:"Nunito Sans",sans-serif;color:var(--ink)}

.side{position:absolute;left:60px;width:780px;overflow:hidden;box-shadow:4px 6px 8px rgba(0,0,0,.25)}
.side-front{top:28px;height:552px}
.side-back{top:600px;height:550px}

.front-backdrop{position:absolute;inset:0;background:radial-gradient(ellipse at 50% 65%,#e6e3df 0%,#f4f3f2 55%,#f7f7f6 100%)}
.front-band{position:absolute;left:0;top:0;width:780px;height:300px}
.front-photo{position:absolute;left:215px;top:50px;width:353px;height:214px;background:linear-gradient(160deg,#f2f0ee 0%,#d9d4cf 55%,#a98a66 100%)}
.front-photo-name{position:absolute;left:215px;top:62px;width:353px;text-align:center;font-family:"Caveat",cursive;font-size:30px;letter-spacing:6px;color:var(--blue)}
.front-caption{position:absolute;left:208px;top:264px;width:367px;height:38px;background:var(--purple);color:var(--white);font-family:"Caveat",cursive;font-size:17px;text-align:center;line-height:38px}
.front-ornament{position:absolute;left:268px;top:302px;width:250px;height:100px;border-radius:0 0 125px 125px;background:radial-gradient(ellipse at 50% 0%,rgba(108,69,155,.75) 0%,rgba(108,69,155,.35) 45%,rgba(108,69,155,.08) 80%)}
.front-name{position:absolute;left:0;top:392px;width:780px;text-align:center;font-family:"Caveat",cursive;font-size:40px;letter-spacing:8px;color:var(--blue)}
.front-contact{position:absolute;left:0;top:482px;width:780px;text-align:center;font-weight:600;font-size:15.5px;line-height:22px;color:var(--blue)}
.front-contact span+span{margin-left:10px}

.back-photo{position:absolute;inset:0;background:linear-gradient(90deg,#f3f2f0 0%,#e9e6e3 40%,#e2dcd5 60%,#f1f0ee 100%)}
.back-floor{position:absolute;left:0;right:0;bottom:0;height:110px;background:linear-gradient(180deg,#cbb08a,#b99a70)}
.back-name{position:absolute;left:42px;top:14px;font-family:"Caveat",cursive;font-size:30px;letter-spacing:13px;color:rgba(150,150,150,.28)}
.edge-rule{position:absolute;height:1px;background:#9a9a9a}

.timetable{position:absolute;left:60px;top:36px;width:670px;height:442px;background:rgba(235,235,237,.78);border-radius:10px}
.tt-head{position:absolute;left:60px;top:63px;width:670px;height:21px;background:var(--purple-deep);color:var(--white);font-size:12.5px;letter-spacing:.5px;line-height:21px}
.tt-head span{position:absolute;top:0;transform:translateX(-50%);font-weight:700}
.tt-head .tt-timeline{font-weight:400;left:30px;transform:none}

.tt-row{position:absolute;left:0;width:780px;height:1px}
.tt-line{position:absolute;left:160px;width:507px;top:0;height:1px;background:var(--rule)}
.tt-dot{position:absolute;left:158px;top:-1px;width:3px;height:3px;border-radius:50%;background:var(--rule)}
.tt-time{position:absolute;right:652px;top:-9px;font-family:"Arimo",sans-serif;font-weight:700;font-size:12px;white-space:nowrap}
.tt-time small{font-size:7px;font-weight:400;position:relative;top:5px;margin-left:1px}

.class{position:absolute;width:62px;height:22px;margin-left:-31px;top:-11px;border:1px solid #555;border-radius:3px;font-family:"Arimo",sans-serif;font-size:8.5px;line-height:20px;text-align:center;color:#333;box-shadow:1px 1px 1px rgba(0,0,0,.2)}
.class.two-line{line-height:10px;padding-top:1px}
.class.booking::after{content:"*";position:absolute;right:2px;top:-6px;color:var(--star);font-size:12px}
.rise{background:var(--c-rise)}
.vinyasa{background:var(--c-vinyasa)}
.yin{background:var(--c-yin)}
.slow{background:var(--c-slow)}
.preg{background:var(--c-preg)}
.mum{background:var(--c-mum)}
.kids-older{background:var(--c-kids-older)}
.kids-young{background:var(--c-kids-young)}
.teens{background:var(--c-teens)}
.restore{background:var(--c-restore)}
.yin-restore{background:#e3e3e3}
.women{background:var(--c-women)}

.tt-foot{position:absolute;left:60px;top:488px;width:670px;height:28px;background:rgba(245,243,241,.85);font-size:12.5px;line-height:28px;padding-left:46px}
.tt-foot b{color:var(--star);font-weight:400;margin-right:4px}
.tt-web{position:absolute;left:752px;top:380px;transform:translate(-50%,-50%) rotate(90deg);font-family:"Arimo",sans-serif;font-weight:700;font-size:15px;color:var(--purple-deep);white-space:nowrap;letter-spacing:.3px}
</style>
</head>
<body>

<section class="side side-front">
  <div class="front-backdrop" role="img" aria-label="Faded photo of a yoga student in a wide standing pose in a bright studio"></div>
  <svg class="front-band" viewBox="0 0 780 300" aria-hidden="true">
    <path d="M0 0H780V196C700 182 640 178 580 190L220 272C130 274 45 240 0 190Z" fill="#c9bfb2"/>
    <path d="M0 0H780V188C700 174 640 170 580 182L220 264C130 266 45 232 0 182Z" fill="var(--purple)"/>
  </svg>
  <div class="front-photo" role="img" aria-label="Photo of a yoga student in downward dog on a woven floor mat"></div>
  <div class="front-photo-name">fennel stretch hall</div>
  <div class="front-caption">Inclusive, inspiring boutique yoga studio classes for all ages</div>
  <div class="front-ornament" role="img" aria-label="Purple mandala ornament"></div>
  <div class="front-name">fennel stretch hall</div>
  <div class="front-contact">
    <div>4/71 Wexcombe Lane, Pelharton</div>
    <div><span>mobile: 0471 296 814</span><span>website: fennelstretch.com.au</span></div>
  </div>
</section>

<section class="side side-back">
  <div class="back-photo" role="img" aria-label="Faded photo of a yoga student in a side angle pose"></div>
  <div class="back-floor" role="img" aria-label="Woven studio floor"></div>
  <div class="back-name">fennel stretch hall</div>

  <div class="timetable"></div>
  <div class="tt-head">
    <span class="tt-timeline">TIMELINE</span>
    <span style="left:163px">MON</span><span style="left:227px">TUE</span><span style="left:301px">WED</span>
    <span style="left:367px">THU</span><span style="left:436px">FRI</span><span style="left:507px">SAT</span><span style="left:578px">SUN</span>
  </div>

  <div class="edge-rule" style="left:0;width:45px;top:112px"></div><div class="edge-rule" style="left:745px;width:35px;top:112px"></div>
  <div class="edge-rule" style="left:0;width:45px;top:141px"></div><div class="edge-rule" style="left:745px;width:35px;top:141px"></div>
  <div class="edge-rule" style="left:0;width:45px;top:170px"></div><div class="edge-rule" style="left:745px;width:35px;top:170px"></div>
  <div class="edge-rule" style="left:0;width:45px;top:198px"></div><div class="edge-rule" style="left:745px;width:35px;top:198px"></div>
  <div class="edge-rule" style="left:0;width:45px;top:227px"></div><div class="edge-rule" style="left:745px;width:35px;top:227px"></div>
  <div class="edge-rule" style="left:0;width:45px;top:255px"></div><div class="edge-rule" style="left:745px;width:35px;top:255px"></div>

  <div class="tt-row" style="top:112px"><i class="tt-line"></i><i class="tt-dot"></i><div class="tt-time">5:45<small>AM</small></div>
    <div class="class rise booking" style="left:287px">Rise + Shine</div><div class="class rise booking" style="left:427px">Rise + Shine</div></div>
  <div class="tt-row" style="top:141px"><i class="tt-line"></i><i class="tt-dot"></i><div class="tt-time">9:00<small>AM</small></div>
    <div class="class vinyasa" style="left:567px">Vinyasa Flow</div></div>
  <div class="tt-row" style="top:170px"><i class="tt-line"></i><i class="tt-dot"></i><div class="tt-time">9:15<small>AM</small></div>
    <div class="class vinyasa" style="left:287px">Vinyasa Flow</div><div class="class yin" style="left:636px">Yin</div></div>
  <div class="tt-row" style="top:198px"><i class="tt-line"></i><i class="tt-dot"></i><div class="tt-time">9:30<small>AM</small></div>
    <div class="class slow" style="left:219px">Slow Flow</div><div class="class vinyasa" style="left:427px">Vinyasa Flow</div></div>
  <div class="tt-row" style="top:227px"><i class="tt-line"></i><i class="tt-dot"></i><div class="tt-time">10:30<small>AM</small></div>
    <div class="class preg booking" style="left:567px">Pregnancy</div></div>
  <div class="tt-row" style="top:255px"><i class="tt-line"></i><i class="tt-dot"></i><div class="tt-time">11:00<small>PM</small></div>
    <div class="class mum booking" style="left:287px">Mum + Baby</div><div class="class mum booking" style="left:427px">Mum + Baby</div></div>
  <div class="tt-row" style="top:284px"><i class="tt-line"></i><i class="tt-dot"></i><div class="tt-time">12:15<small>PM</small></div>
    <div class="class preg booking" style="left:427px">Pregnancy</div></div>
  <div class="tt-row" style="top:312px"><i class="tt-line"></i><i class="tt-dot"></i><div class="tt-time">4:00<small>PM</small></div>
    <div class="class kids-older booking" style="left:358px">Kids 8-12</div><div class="class kids-young booking" style="left:427px">Kids 5-7</div><div class="class vinyasa" style="left:567px">Vinyasa Flow</div></div>
  <div class="tt-row" style="top:341px"><i class="tt-line"></i><i class="tt-dot"></i><div class="tt-time">4:45<small>PM</small></div>
    <div class="class teens booking" style="left:358px">Teens 12-16</div></div>
  <div class="tt-row" style="top:370px"><i class="tt-line"></i><i class="tt-dot"></i><div class="tt-time">5:00<small>PM</small></div>
    <div class="class teens booking" style="left:427px">Teens 12-16</div></div>
  <div class="tt-row" style="top:398px"><i class="tt-line"></i><i class="tt-dot"></i><div class="tt-time">6:00<small>PM</small></div>
    <div class="class preg booking" style="left:219px">Pregnancy</div><div class="class vinyasa" style="left:289px">Vinyasa Flow</div><div class="class slow" style="left:358px">Slow Flow</div><div class="class restore" style="left:497px">Flow + Restore</div></div>
  <div class="tt-row" style="top:427px"><i class="tt-line"></i><i class="tt-dot"></i><div class="tt-time">6:15<small>PM</small></div>
    <div class="class preg booking" style="left:427px">Pregnancy</div></div>
  <div class="tt-row" style="top:456px"><i class="tt-line"></i><i class="tt-dot"></i><div class="tt-time">7:30<small>PM</small></div>
    <div class="class vinyasa" style="left:219px">Vinyasa Flow</div><div class="class preg booking" style="left:289px">Pregnancy</div><div class="class yin-restore" style="left:358px">Yin + Restore</div><div class="class women two-line booking" style="left:427px">Women's<br>Wellness</div></div>

  <div class="tt-foot"><b>*</b>Bookings essential</div>
  <div class="tt-web">www.fennelstretch.com.au</div>
</section>

</body>
</html>
```